Business card design for Tolvin Waste

I would like double-sided business cards for myself and my partner that includes our logo and the existing colour scheme. We provide waste and environmental services to customers in the motor-vehicle and engineering industries.

```html
<!DOCTYPE html>
<html lang="en">
<head>
<meta charset="utf-8">
<title>Tolvin Waste – Business Cards</title>
<link href="https://fonts.googleapis.com/css2?family=Lato:wght@400;700;900&display=swap" rel="stylesheet">
<style>
  :root {
    --page-bg: #2e2f31;
    --card-bg: #1d1e20;
    --card-pattern: #242527;
    --green: #8cc63f;
    --white: #ffffff;
    --text-grey: #c9c9c9;
    --rule: #6a6a6a;
  }
  * { margin: 0; padding: 0; box-sizing: border-box; }
  html, body { width: 1200px; height: 1108px; overflow: hidden; }
  body {
    background: var(--page-bg);
    font-family: 'Lato', sans-serif;
    position: relative;
  }
  .card {
    position: absolute;
    top: 214px;
    width: 420px;
    height: 680px;
    background: var(--card-bg);
    border-radius: 22px;
    overflow: hidden;
  }
  .card--front { left: 150px; }
  .card--back { left: 630px; }

  .brand {
    display: flex;
    align-items: center;
    gap: 14px;
  }
  .brand__dot {
    border-radius: 50%;
    border: 5px solid var(--green);
    flex: none;
  }
  .brand__name {
    font-family: 'Lato', sans-serif;
    font-weight: 900;
    color: var(--white);
    text-transform: uppercase;
    line-height: 1;
  }

  .card--front .brand { position: absolute; top: 120px; left: 42px; }
  .card--front .brand__dot { width: 72px; height: 72px; }
  .card--front .brand__name { font-size: 40px; letter-spacing: 1px; }

  .details {
    position: absolute;
    top: 330px;
    left: 0;
    right: 0;
    text-align: center;
    color: var(--text-grey);
  }
  .details__name {
    color: var(--green);
    font-size: 27px;
    font-weight: 400;
    text-transform: uppercase;
  }
  .details__role { font-size: 19px; margin-top: 2px; }
  .icon-rule {
    display: flex;
    align-items: center;
    justify-content: center;
    gap: 6px;
    margin: 16px auto 12px;
    width: 300px;
  }
  .icon-rule__line { flex: 1; height: 1px; background: var(--rule); }
  .icon-rule__icon {
    width: 22px; height: 22px; border-radius: 50%;
    background: var(--green);
    display: flex; align-items: center; justify-content: center;
  }
  .details__line { font-size: 19px; line-height: 1.35; }
  .rule {
    width: 300px; height: 1px; background: var(--rule);
    margin: 14px auto;
  }

  .pattern-field {
    position: absolute;
    inset: 0;
    background: var(--card-pattern);
  }
  .card--back .brand {
    position: absolute;
    right: 38px;
    bottom: 92px;
    flex-direction: column;
    align-items: flex-end;
    gap: 18px;
  }
  .card--back .brand__dot { width: 50px; height: 50px; }
  .card--back .brand__name { font-size: 54px; text-align: right; letter-spacing: 1px; }
</style>
</head>
<body>

  <section class="card card--front" aria-label="Business card front">
    <div class="brand">
      <span class="brand__dot"></span>
      <span class="brand__name">Tolvin Waste</span>
    </div>

    <div class="details">
      <p class="details__name">Daniel Reeve</p>
      <p class="details__role">Managing Director</p>

      <div class="icon-rule">
        <span class="icon-rule__line"></span>
        <span class="icon-rule__icon">
          <svg width="12" height="12" viewBox="0 0 24 24"><path fill="#1d1e20" d="M6.6 10.8a15 15 0 0 0 6.6 6.6l2.2-2.2a1 1 0 0 1 1-.25 11.4 11.4 0 0 0 3.6.6 1 1 0 0 1 1 1V20a1 1 0 0 1-1 1A17 17 0 0 1 3 4a1 1 0 0 1 1-1h3.5a1 1 0 0 1 1 1c0 1.25.2 2.45.6 3.6a1 1 0 0 1-.25 1z"/></svg>
        </span>
        <span class="icon-rule__icon">
          <svg width="12" height="12" viewBox="0 0 24 24"><rect x="3" y="6" width="18" height="12" rx="1" fill="#1d1e20"/><path d="M3 7l9 6 9-6" stroke="#8cc63f" stroke-width="1.6" fill="none"/></svg>
        </span>
        <span class="icon-rule__icon">
          <svg width="12" height="12" viewBox="0 0 24 24"><path fill="#1d1e20" d="M12 2a7 7 0 0 0-7 7c0 5 7 13 7 13s7-8 7-13a7 7 0 0 0-7-7zm0 9.5A2.5 2.5 0 1 1 12 6.5a2.5 2.5 0 0 1 0 5z"/></svg>
        </span>
        <span class="icon-rule__line"></span>
      </div>

      <p class="details__line">444 555 7120</p>
      <p class="details__line">info@tolvinwaste.com</p>
      <p class="details__line">www.tolvinwaste.com</p>
      <div class="rule"></div>
      <p class="details__line">18 Forge Lane,</p>
      <p class="details__line">Brackley, 45318</p>
    </div>
  </section>

  <section class="card card--back" aria-label="Business card back">
    <div class="pattern-field" role="img" aria-label="Faint repeating brand pattern across the card back"></div>
    <div class="brand">
      <span class="brand__dot"></span>
      <span class="brand__name">Tolvin<br>Waste</span>
    </div>
  </section>

</body>
</html>
```